Wattlebloom Berry Farm

I would like the our logo
a mixture of berries
and a kookaburra
Mark & Helen Dorsendi
Farm Fresh & Frozen Strawberries Raspberries & other berries
Homemade award winning Jams, Syrups & Vinegars
ph: 0493517604
Email: helmar@quorvanet.com.au
web www.wattlebloom.com.au
48 Fenwick Road Wandin Vic 3139
BUY DIRECT FROM FARM

Farm

```html
<!DOCTYPE html>
<html lang="en">
<head>
<meta charset="utf-8">
<title>Wattlebloom Berry Farm – Business Card</title>
<link rel="stylesheet" href="https://fonts.googleapis.com/css2?family=Lato:wght@400;700&display=swap">
<style>
  :root {
    --page-bg: #e9e7e4;
    --card-white: #ffffff;
    --farm-green: #1d7a3a;
    --band-green: #13733a;
    --band-green-light: #2a8f4c;
    --berry-red: #b3202a;
    --text-green: #1f6f36;
  }
  * { margin: 0; padding: 0; box-sizing: border-box; }
  html, body {
    width: 1200px; height: 818px; overflow: hidden;
    background: var(--page-bg);
    font-family: "Lato", sans-serif;
  }
  .stage {
    width: 1200px; height: 818px;
    display: flex; align-items: center; justify-content: center;
  }
  .business-card {
    position: relative;
    width: 900px; height: 514px;
    background: var(--card-white);
    box-shadow: 0 10px 30px rgba(0,0,0,0.18);
    overflow: hidden;
    color: var(--text-green);
  }
  .brand {
    position: absolute; left: 44px; top: 40px;
    display: flex; align-items: center; gap: 16px;
  }
  .brand-mark {
    width: 96px; height: 96px; border-radius: 50%;
    background: var(--farm-green);
  }
  .brand-name {
    font-weight: 700; font-size: 26px; color: var(--farm-green);
  }
  .owners {
    position: absolute; left: 400px; top: 176px;
    font-weight: 700; font-size: 32px;
    text-decoration: underline; text-underline-offset: 5px;
    color: var(--farm-green);
  }
  .address {
    position: absolute; left: 400px; top: 226px;
    display: flex; align-items: center; gap: 8px;
    font-size: 21px;
  }
  .contact-row {
    position: absolute; left: 44px;
    display: flex; align-items: center; gap: 10px;
    font-size: 21px;
  }
  .contact-row svg, .address svg { flex: none; fill: var(--text-green); }
  .phone { top: 220px; }
  .email { top: 272px; left: 280px; }
  .web { top: 272px; left: 640px; }
  .offer {
    position: absolute; left: 44px; right: 44px; top: 320px;
    text-align: center; font-size: 22px; line-height: 1.4;
  }
  .band-stripe {
    position: absolute; left: 0; right: 0; top: 420px; height: 8px;
    background: var(--berry-red);
  }
  .band {
    position: absolute; left: 0; right: 0; top: 428px; bottom: 0;
    background: linear-gradient(180deg, var(--band-green-light), var(--band-green));
    display: flex; align-items: center; justify-content: center;
    color: #ffffff; font-size: 24px; letter-spacing: 1px;
  }
</style>
</head>
<body>
<main class="stage">
  <article class="business-card">
    <header class="brand">
      <div class="brand-mark"></div>
      <span class="brand-name">Wattlebloom Berry Farm</span>
    </header>

    <h1 class="owners">Mark &amp; Helen Dorsendi</h1>
    <p class="address">
      <svg width="16" height="20" viewBox="0 0 16 20"><path d="M8 0a7 7 0 0 0-7 7c0 5 7 13 7 13s7-8 7-13a7 7 0 0 0-7-7zm0 10a3 3 0 1 1 0-6 3 3 0 0 1 0 6z"/></svg>
      48 Fenwick Road Wandin Vic 3139
    </p>

    <p class="contact-row phone">
      <svg width="24" height="20" viewBox="0 0 24 20"><path d="M2 6c0-3 4-5 10-5s10 2 10 5v2h-5V6H7v2H2zM5 9h14l3 10H2z"/></svg>
      0493517604
    </p>
    <p class="contact-row email">
      <svg width="24" height="18" viewBox="0 0 24 18"><path d="M0 0h24v18H0zM2 2v1l10 7 10-7V2zm0 3v11h20V5l-10 7z"/></svg>
      helmar@quorvanet.com.au
    </p>
    <p class="contact-row web">
      <svg width="20" height="20" viewBox="0 0 20 20"><circle cx="10" cy="10" r="10"/><path d="M5 6c2 0 3 1 3 3s-2 2-2 4-2 1-2-1-1-2-1-3 1-3 2-3zm8 1c2 1 3 3 2 5s-3 3-3 1 1-3 0-4-1-2 1-2z" fill="#fff"/></svg>
      wattlebloom.com.au
    </p>

    <p class="offer">
      Farm Fresh &amp; Frozen Strawberries Raspberries &amp; other berries<br>
      Homemade award winning Jams, Syrups &amp; Vinegars
    </p>

    <div class="band-stripe"></div>
    <footer class="band">BUY DIRECT FROM FARM</footer>
  </article>
</main>
</body>
</html>
```